Homemaking training schools needs a Business Card design

Designer, Hello!

No special requirements, good-looking enough.
--------------------------------------------------------------------------

Name: Marcus Liao
Chairman
Tel: 0574-57418263
Mobile: 13852247106
Email: kelvory@mailpond.com
Web: www.tqb2031.com
Add: No.258, LinfengJie, DaoyueQu, Ningbo, Zhejiang

LOGO
Ningbo TQB Homemaking Training School

Target Market(s)

pregnant women, mothers, infants, the elderly and families, including cleaning, cooking, nursing training.

Industry/Entity Type

Business

Contact Information for Business Card

Name: Marcus Liao
Chairman
Tel: 0574-57418263
Mobile: 13852247106
Email: kelvory@mailpond.com
Web: www.tqb2031.com

LOGO

Font styles to use
Serif
Sans Serif
Decorative

Requirements
Nice to have
• Feels: clean, specifications, safety, comfort, warmth and happiness.

```html
<!DOCTYPE html>
<html lang="en">
<head>
<meta charset="utf-8">
<title>TianQiaoBao Business Card</title>
<link href="https://fonts.googleapis.com/css2?family=Quicksand:wght@500;600&family=Crimson+Pro:wght@400;700&family=Open+Sans:wght@500&display=swap" rel="stylesheet">
<style>
  :root {
    --brand-blue: #0a76bd;
    --card-white: #f5f7f7;
    --backdrop: #e8e7e4;
    --icon-grey: #9c9c9c;
    --ink-navy: #1f4f7c;
    --ink-grey: #4a4a4a;
  }
  * { margin: 0; padding: 0; box-sizing: border-box; }
  html, body { width: 1200px; height: 1194px; overflow: hidden; }
  body { background: var(--backdrop); position: relative; }

  .card {
    position: absolute;
    width: 794px;
    height: 515px;
    overflow: hidden;
    box-shadow: 0 4px 14px rgba(0,0,0,0.18);
  }
  .card--front { left: 216px; top: 55px; background: var(--brand-blue); }
  .card--back { left: 214px; top: 622px; background: var(--card-white); }

  .front-panel { position: absolute; inset: 0; }

  .brand {
    position: absolute;
    left: 96px;
    top: 268px;
    width: 384px;
    text-align: center;
  }
  .brand__name {
    font-family: "Quicksand", sans-serif;
    font-weight: 600;
    font-size: 62px;
    line-height: 1;
    color: var(--brand-blue);
    letter-spacing: -0.5px;
  }
  .brand__tagline {
    display: flex;
    align-items: center;
    gap: 8px;
    margin-top: 6px;
    font-family: "Quicksand", sans-serif;
    font-weight: 500;
    font-size: 22px;
    color: var(--ink-grey);
    white-space: nowrap;
  }
  .brand__rule { flex: 1; height: 2px; background: #333; }

  .back-band {
    position: absolute;
    left: 0; top: 0;
    width: 100%;
    height: 256px;
    background: var(--brand-blue);
  }
  .holder {
    position: absolute;
    left: 119px;
    top: 108px;
    font-family: "Crimson Pro", serif;
    font-weight: 700;
    color: #fff;
  }
  .holder__name { font-size: 56px; line-height: 1; letter-spacing: 0.5px; }
  .holder__role { font-size: 30px; line-height: 1; margin-top: 6px; letter-spacing: 0.5px; }
  .website {
    position: absolute;
    left: 500px;
    top: 224px;
    font-family: "Open Sans", sans-serif;
    font-weight: 500;
    font-size: 18px;
    color: #fff;
    letter-spacing: 0.4px;
  }

  .tabs { position: absolute; left: 0; top: 0; }

  .contact {
    position: absolute;
    display: flex;
    align-items: center;
    gap: 12px;
    font-family: "Crimson Pro", serif;
    font-size: 20px;
    color: var(--ink-navy);
  }
  .contact__icon { width: 29px; height: 29px; flex: none; }
  .contact--mobile { left: 117px; top: 287px; }
  .contact--phone { left: 117px; top: 337px; }
  .contact--email { left: 117px; top: 382px; }
  .contact--address { left: 455px; top: 288px; align-items: flex-start; line-height: 26px; }
</style>
</head>
<body>

  <section class="card card--front" aria-label="Card front">
    <svg class="front-panel" width="794" height="515" viewBox="0 0 794 515">
      <path d="M0 156 H636 C636 305 520 419 384 419 H0 Z" fill="var(--card-white)"/>
    </svg>
    <div class="brand">
      <div class="brand__name">TianQiaoBao</div>
      <div class="brand__tagline">
        <span class="brand__rule"></span>
        <span>Training &amp; Services</span>
        <span class="brand__rule"></span>
      </div>
    </div>
  </section>

  <section class="card card--back" aria-label="Card back">
    <div class="back-band"></div>
    <div class="holder">
      <div class="holder__name">MARCUS LIAO</div>
      <div class="holder__role">CHAIRMAN</div>
    </div>
    <div class="website">www.tqb2031.com</div>

    <svg class="tabs" width="120" height="515" viewBox="0 0 120 515">
      <path d="M0 284 H86 L106 301.5 L86 319 H0 Z" fill="var(--brand-blue)"/>
      <path d="M0 334 H86 L106 352 L86 370 H0 Z" fill="var(--brand-blue)"/>
      <path d="M0 383 H86 L106 401 L86 419 H0 Z" fill="var(--brand-blue)"/>
    </svg>

    <div class="contact contact--mobile">
      <svg class="contact__icon" viewBox="0 0 30 30">
        <circle cx="15" cy="15" r="15" fill="var(--icon-grey)"/>
        <rect x="11" y="7" width="8" height="16" rx="1.5" fill="#fff"/>
        <rect x="12.3" y="9" width="5.4" height="10" fill="var(--icon-grey)"/>
      </svg>
      <span>13852247106</span>
    </div>

    <div class="contact contact--phone">
      <svg class="contact__icon" viewBox="0 0 30 30">
        <circle cx="15" cy="15" r="15" fill="var(--icon-grey)"/>
        <path d="M9 8 L12 7.5 L13.5 11.5 L11.6 13 C12.6 15.3 14.5 17.3 17 18.4 L18.5 16.5 L22.5 18 L22 21 C21.5 22.3 19.5 22.6 17.5 21.8 C13 20 10 17 8.3 12.5 C7.6 10.5 7.8 8.6 9 8 Z" fill="#fff"/>
      </svg>
      <span>0574-57418263</span>
    </div>

    <div class="contact contact--email">
      <svg class="contact__icon" viewBox="0 0 30 30">
        <circle cx="15" cy="15" r="15" fill="var(--icon-grey)"/>
        <rect x="8" y="10" width="14" height="10" rx="1" fill="#fff"/>
        <path d="M8.5 10.5 L15 15.5 L21.5 10.5" fill="none" stroke="var(--icon-grey)" stroke-width="1.2"/>
      </svg>
      <span>kelvory@mailpond.com</span>
    </div>

    <div class="contact contact--address">
      <svg class="contact__icon" viewBox="0 0 30 30" style="margin-top:2px">
        <circle cx="15" cy="15" r="15" fill="var(--icon-grey)"/>
        <path d="M15 7 C11.9 7 10 9.2 10 11.8 C10 15.3 15 21.5 15 21.5 C15 21.5 20 15.3 20 11.8 C20 9.2 18.1 7 15 7 Z" fill="#fff"/>
        <circle cx="15" cy="11.8" r="1.9" fill="var(--icon-grey)"/>
      </svg>
      <span>No.258, LinfengJie,<br>DaoyueQu, Ningbo, Zhejiang</span>
    </div>
  </section>

</body>
</html>
```